New Interrior Decoration company needs new website

We need a website for our new company specialising in interior decoration to residential and commercial markets.
We supply and install decorative and printed films for office and home decoration such as feature walls.
We would like to keep the design simple and clean.

Target Market(s)

Architects and interior designaers

Industry/Entity Type

It Company

Number of Pages Required

5+ page

Font styles to use
Sans Serif

Requirements
Must have
• Home page,
• Services/products page (split into commercial and residential)
• Gallery (split into commercial and residential)
• contact form and page
Nice to have
• Very clean and minimalistic design.

```html
<!DOCTYPE html>
<html lang="en">
<head>
<meta charset="utf-8">
<title>Lumen Interiors — Residential &amp; Commercial Interior Design</title>
<link href="https://fonts.googleapis.com/css2?family=Montserrat:wght@200;300;400;500;600;700&family=Open+Sans:wght@400;600&display=swap" rel="stylesheet">
<style>
:root{
  --blue:#1e88e5;
  --blue-dark:#1565c0;
  --ink:#222428;
  --text:#555a60;
  --muted:#8a8f95;
  --line:#e3e5e8;
  --soft:#f4f5f6;
  --white:#ffffff;
  --footer:#1b1c22;
  --footer-line:#34363e;
}
*{margin:0;padding:0;box-sizing:border-box}
html,body{width:1200px;height:2609px;overflow:hidden;background:var(--white)}
body{position:relative;font-family:"Montserrat",Arial,sans-serif;color:var(--ink)}
.abs{position:absolute}
.center{left:0;width:1200px;text-align:center}

/* header */
.site-header{position:absolute;left:0;top:0;width:1200px;height:92px;background:var(--white)}
.brand{position:absolute;left:157px;top:22px;display:flex;align-items:center;gap:10px}
.brand-mark{width:40px;height:40px;background:var(--blue)}
.brand-name{font-weight:700;font-size:25px;line-height:24px;text-transform:uppercase;color:var(--ink);letter-spacing:-.5px}
.tollfree{position:absolute;right:157px;top:17px;font-size:15px;color:var(--blue);letter-spacing:.5px}
.main-nav{position:absolute;top:54px;left:0;width:1200px;font-size:11px;letter-spacing:1px;color:var(--muted)}
.main-nav span{position:absolute}
.main-nav .active{color:var(--blue)}

/* hero */
.hero{position:absolute;left:0;top:92px;width:1200px;height:440px;background:linear-gradient(180deg,#8f9499 0%,#b8bbbe 40%,#7b756d 75%,#4e3f33 100%)}
.hero-kicker{top:228px;font-size:30px;font-weight:500;color:var(--white)}
.hero-title{top:274px;font-size:50px;font-weight:200;letter-spacing:3px;color:var(--white)}
.btn{position:absolute;display:flex;align-items:center;justify-content:center;font-size:11px;font-weight:600;letter-spacing:1px;text-transform:uppercase}
.btn-blue{background:var(--blue);color:var(--white)}
.btn-white{background:var(--white);color:var(--ink)}
.hero-arrow{position:absolute;top:285px}

/* intro */
.intro-title{top:582px;font-size:24px;font-weight:500;line-height:34px;text-transform:uppercase}
.intro-title em{font-style:normal;color:var(--blue)}
.intro-sub{top:647px;font-family:"Open Sans",Arial,sans-serif;font-size:15px;color:var(--text)}
.cat{position:absolute;top:704px;width:180px;text-align:center}
.cat-icon{width:60px;height:60px;margin:0 auto;border-radius:50%;border:1px solid var(--line);background:var(--white);display:flex;align-items:center;justify-content:center}
.cat-icon.active{background:var(--blue);border-color:var(--blue)}
.cat-label{margin-top:12px;font-size:13px;letter-spacing:.5px;text-transform:uppercase;color:var(--ink)}

.portfolio-panel{position:absolute;left:0;top:814px;width:1200px;height:496px;border-top:1px solid var(--line)}
.tile{position:absolute;width:279px;height:167px}
.tile-caption{position:absolute;left:0;bottom:0;width:100%;height:36px;background:rgba(40,40,40,.72);color:var(--white);font-size:13px;font-weight:600;display:flex;align-items:center;justify-content:center}
.dot{position:absolute;top:1250px;width:11px;height:11px;border-radius:50%;background:#c6c9cc}
.dot.active{background:var(--blue)}

/* latest projects */
.projects{position:absolute;left:0;top:1310px;width:1200px;height:436px;background:var(--soft)}
.section-title{font-size:19px;font-weight:500;text-transform:uppercase;letter-spacing:.5px}
.section-sub{font-family:"Open Sans",Arial,sans-serif;font-size:13px;color:var(--text)}
.strip-tile{position:absolute;top:1421px;width:240px;height:212px}
.strip-overlay{background:rgba(30,136,229,.9);color:var(--white);font-size:14px;text-align:center;display:flex;flex-direction:column;justify-content:center;text-transform:none}

/* news */
.news-title{font-size:18px;font-weight:600;text-transform:uppercase}
.post{position:absolute;top:1843px;width:418px}
.post-image{width:418px;height:235px}
.post-title{margin-top:20px;font-size:18px;font-weight:500}
.post-date{margin-top:6px;font-family:"Open Sans",Arial,sans-serif;font-size:11px;color:var(--muted)}
.post-body{margin-top:10px;font-family:"Open Sans",Arial,sans-serif;font-size:11.5px;line-height:16px;color:var(--text)}
.post-more{margin-top:16px;font-family:"Open Sans",Arial,sans-serif;font-size:12px;color:var(--text)}
.post-more.hover{color:var(--blue)}

/* footer */
.site-footer{position:absolute;left:0;top:2289px;width:1200px;height:320px;background:var(--footer);color:var(--white)}
.footer-heading{position:absolute;top:52px;font-size:18px;font-weight:500;text-transform:uppercase}
.contact-col{position:absolute;top:118px;width:228px;text-align:center}
.contact-col h4{font-size:14px;font-weight:600}
.contact-col p{margin-top:8px;font-family:"Open Sans",Arial,sans-serif;font-size:11.5px;line-height:19px;color:#d6d8dc}
.col-divider{position:absolute;top:2405px;width:1px;height:74px;background:var(--footer-line)}
.social{display:flex;justify-content:center;gap:14px;margin-top:14px}
.social span{width:11px;height:11px;border-radius:50%;background:#d6d8dc}
.social span.hover{background:var(--blue)}
.footer-rule{position:absolute;left:0;top:2518px;width:1200px;height:1px;background:var(--footer-line)}
.copyright{position:absolute;left:157px;top:2551px;font-family:"Open Sans",Arial,sans-serif;font-size:11.5px;color:#c8cace}
.footer-nav{position:absolute;top:2551px;left:590px;font-size:11.5px;color:#c8cace;letter-spacing:.5px}
.footer-nav .active{color:var(--blue)}
.footer-nav i{font-style:normal;margin:0 10px;color:#666a72}
</style>
</head>
<body>

<header class="site-header">
  <div class="brand"><div class="brand-mark"></div><div class="brand-name">Lumen<br>Interiors</div></div>
  <div class="tollfree">TOLL FREE: 800 555 0142</div>
  <nav class="main-nav">
    <span class="active" style="left:545px">- HOME -</span>
    <span style="left:624px">ABOUT US</span>
    <span style="left:723px">SERVICES</span>
    <span style="left:822px">GALLERY</span>
    <span style="left:913px">CONTACT US</span>
    <svg class="abs" style="left:1030px;top:0" width="12" height="12" viewBox="0 0 12 12"><circle cx="5" cy="5" r="3.6" fill="none" stroke="#555a60" stroke-width="1.5"/><line x1="7.6" y1="7.6" x2="11" y2="11" stroke="#555a60" stroke-width="1.6"/></svg>
  </nav>
</header>

<section class="hero" role="img" aria-label="Bright living room with a white sectional sofa, glass coffee table, tall planter and dark wood floor"></section>
<div class="abs center hero-kicker">Residential &amp; Commercial</div>
<div class="abs center hero-title">INTERIOR DESIGN</div>
<div class="btn btn-blue" style="left:476px;top:360px;width:112px;height:28px">Get a Quote</div>
<div class="btn btn-white" style="left:605px;top:360px;width:118px;height:28px">Our Projects</div>
<svg class="hero-arrow" style="left:64px" width="28" height="56" viewBox="0 0 28 56"><polyline points="24,4 4,28 24,52" fill="none" stroke="#fff" stroke-width="2.5"/></svg>
<svg class="hero-arrow" style="left:1108px" width="28" height="56" viewBox="0 0 28 56"><polyline points="4,4 24,28 4,52" fill="none" stroke="#fff" stroke-width="2.5"/></svg>

<section>
  <h2 class="abs center intro-title">See why over <em>1,000.00+ customers</em> have<br>chosen Lumen Interiors</h2>
  <p class="abs center intro-sub">Be inspired! Browse our portfolio</p>

  <div class="cat" style="left:143px"><div class="cat-icon"><svg width="26" height="26" viewBox="0 0 26 26" fill="none" stroke="#555a60" stroke-width="1.5"><rect x="5" y="6" width="7" height="18"/><rect x="12" y="2" width="8" height="22"/><line x1="2" y1="24" x2="24" y2="24"/></svg></div><div class="cat-label">Commercial</div></div>
  <div class="cat" style="left:326px"><div class="cat-icon active"><svg width="26" height="26" viewBox="0 0 26 26" fill="none" stroke="#fff" stroke-width="1.8"><rect x="3" y="11" width="20" height="8" rx="2"/><rect x="6" y="6" width="14" height="6" rx="2"/><line x1="6" y1="19" x2="6" y2="22"/><line x1="20" y1="19" x2="20" y2="22"/></svg></div><div class="cat-label">Living Rooms</div></div>
  <div class="cat" style="left:508px"><div class="cat-icon"><svg width="26" height="26" viewBox="0 0 26 26" fill="none" stroke="#555a60" stroke-width="1.5"><rect x="3" y="12" width="20" height="7"/><rect x="5" y="7" width="8" height="5"/><line x1="3" y1="19" x2="3" y2="22"/><line x1="23" y1="19" x2="23" y2="22"/></svg></div><div class="cat-label">Bedrooms</div></div>
  <div class="cat" style="left:691px"><div class="cat-icon"><svg width="26" height="26" viewBox="0 0 26 26" fill="none" stroke="#555a60" stroke-width="1.5"><rect x="5" y="3" width="16" height="20"/><line x1="13" y1="3" x2="13" y2="23"/><line x1="5" y1="10" x2="21" y2="10"/><line x1="5" y1="16" x2="21" y2="16"/></svg></div><div class="cat-label">Home Offices</div></div>
  <div class="cat" style="left:873px"><div class="cat-icon"><svg width="28" height="26" viewBox="0 0 28 26" fill="none" stroke="#555a60" stroke-width="1.5"><line x1="7" y1="10" x2="21" y2="10"/><line x1="10" y1="10" x2="10" y2="21"/><line x1="18" y1="10" x2="18" y2="21"/><path d="M3 5v16M3 14h4v7M25 5v16M25 14h-4v7"/></svg></div><div class="cat-label">Dining Rooms</div></div>
</section>

<section class="portfolio-panel">
  <svg class="abs" style="left:396px;top:-1px" width="40" height="22" viewBox="0 0 40 22"><polygon points="0,0 20,20 40,0" fill="#fff"/><polyline points="0,1 20,21 40,1" fill="none" stroke="#e3e5e8"/></svg>
</section>
<div class="tile" style="left:157px;top:861px;background:linear-gradient(135deg,#d9e3a0,#b9c86a 50%,#e8e8e4)" role="img" aria-label="Living room with a bold green patterned feature wall and white sofa"><div class="tile-caption">Columbia, MD Living Room</div></div>
<div class="tile" style="left:461px;top:861px;background:linear-gradient(180deg,#7a3d44,#a86c6f 60%,#d8d3ce)" role="img" aria-label="Living room with a burgundy textured feature wall and cream sectional"><div class="tile-caption">Ottawa, ON Living Room</div></div>
<div class="tile" style="left:765px;top:861px;background:linear-gradient(180deg,#4d4c49,#6a6966 60%,#cfcdca)" role="img" aria-label="Living room with a dark stone-effect wall and white sofa"><div class="tile-caption">Columbia, MD Living Room</div></div>
<div class="tile" style="left:157px;top:1052px;background:linear-gradient(135deg,#e7e7e5,#9c9a96 60%,#4a4845)" role="img" aria-label="Open-plan living area with kitchen and colourful cushions"><div class="tile-caption">Bogart, GA Living Room</div></div>
<div class="tile" style="left:461px;top:1052px;background:linear-gradient(135deg,#b8342e,#d9d3cc 55%,#eae6e0)" role="img" aria-label="Living room with a red feature wall and fireplace"><div class="tile-caption">Ottawa, ON Living Room</div></div>
<div class="tile" style="left:765px;top:1052px;background:linear-gradient(135deg,#8ea0ad,#c5bfb5 55%,#8a7561)" role="img" aria-label="Living room with patterned curtains and a stone fireplace"><div class="tile-caption">Columbia, MD Living Room</div></div>
<span class="dot" style="left:574px"></span><span class="dot active" style="left:594px"></span><span class="dot" style="left:614px"></span>

<section class="projects"></section>
<h3 class="abs section-title" style="left:157px;top:1354px">Latest Projects</h3>
<p class="abs section-sub" style="left:157px;top:1381px">Our newest creations</p>
<div class="btn btn-blue" style="left:890px;top:1358px;width:153px;height:32px">View All Projects</div>
<div class="strip-tile" style="left:0;background:linear-gradient(135deg,#bdbab5,#6e6b66 60%,#dcdad6)" role="img" aria-label="Modern kitchen and dining area with pendant globe lights"></div>
<div class="strip-tile strip-overlay" style="left:240px;background:linear-gradient(135deg,#1e88e5,#1a6fc4)" role="img" aria-label="Wood wall project, residential"><div style="font-size:14px;letter-spacing:.5px">WOOD WALL CITY</div><div style="font-size:14px;margin-top:4px">Residential</div></div>
<div class="strip-tile" style="left:480px;background:linear-gradient(135deg,#8a3b2c,#a85a44 45%,#d8d8d6)" role="img" aria-label="Lounge with a brick-effect feature wall and black leather sofa"></div>
<div class="strip-tile" style="left:720px;background:linear-gradient(135deg,#b99d59,#8a7b52 45%,#c9463b 80%)" role="img" aria-label="Room with multicoloured wood-panel wall and red chairs"></div>
<div class="strip-tile" style="left:960px;background:linear-gradient(135deg,#cfd98f,#a7b862 55%,#e6e5e0)" role="img" aria-label="Living room with a green patterned feature wall"></div>
<svg class="abs" style="left:18px;top:1519px" width="10" height="16" viewBox="0 0 10 16"><polyline points="8,1 2,8 8,15" fill="none" stroke="#fff" stroke-width="2"/></svg>
<svg class="abs" style="left:1172px;top:1519px" width="10" height="16" viewBox="0 0 10 16"><polyline points="2,1 8,8 2,15" fill="none" stroke="#1e88e5" stroke-width="2"/></svg>
<div class="btn btn-blue" style="left:508px;top:1666px;width:201px;height:32px">Request a Consultation</div>

<h3 class="abs center news-title" style="top:1803px">Lastest from News</h3>
<article class="post" style="left:157px">
  <div class="post-image" style="background:linear-gradient(135deg,#f2f1ee,#d8d5cf 55%,#a8886a)" role="img" aria-label="Bright dining room with white chairs and a chandelier"></div>
  <h4 class="post-title">2016 Interior Design Trends</h4>
  <div class="post-date">Posted July 5 2016</div>
  <p class="post-body">Morbi vehicula a nibh in commodo. Aliquam quis dolor eget lectus pulvinar eu rhoncus ligula. Ut leo mauris, molestie imperdiet conse-quat in, varius ac sapien.</p>
  <div class="post-more">Read More &rarr;</div>
</article>
<article class="post" style="left:624px">
  <div class="post-image" style="background:linear-gradient(135deg,#c9a56a,#efeae2 45%,#b08a5e)" role="img" aria-label="Sunlit living room with white sofa, staircase and wooden floor"></div>
  <h4 class="post-title">15 Notable Products at Halden Interior Design</h4>
  <div class="post-date">Posted July 5 2016</div>
  <p class="post-body">Morbi vehicula a nibh in commodo. Aliquam quis dolor eget lectus pulvinar eu rhoncus ligula. Ut leo mauris, molestie imperdiet conse-quat in, varius ac sapien.</p>
  <div class="post-more hover">Read More &rarr;</div>
</article>

<footer class="site-footer">
  <h3 class="footer-heading center" style="width:1200px">Get in Touch</h3>
  <div class="contact-col" style="left:143px"><h4>Contact Us</h4><p>info@lumeninteriors.com<br>(040) 555 0199</p></div>
  <div class="contact-col" style="left:373px"><h4>Visit Us</h4><p>48 Harbor Lane district<br>10234 Westfield</p></div>
  <div class="contact-col" style="left:599px"><h4>Office Hours</h4><p>Mon - Fri 9am - 6pm<br>Sat 10am - 2am</p></div>
  <div class="contact-col" style="left:827px"><h4>Follow Us</h4><div class="social"><span></span><span class="hover"></span><span></span><span></span></div></div>
</footer>
<div class="col-divider" style="left:372px"></div>
<div class="col-divider" style="left:600px"></div>
<div class="col-divider" style="left:828px"></div>
<div class="footer-rule"></div>
<div class="copyright">2016 © Lumen Interiors | All Rights Reserved.</div>
<nav class="footer-nav"><span class="active">HOME</span><i>|</i>ABOUT US<i>|</i>SERVICES<i>|</i>GALLERY<i>|</i>CONTACT US</nav>

</body>
</html>
```